BRISKWATER MOTION GYM FLYER DESIGN

We want a flyer designed for our gym. We have an example of a flyer which we like and I have put it into the images I have uploaded. I would like to recreate using our pictures, so its a pretty straight forward job. We also want to put our weekly timetable on the back of the flyer. We would like the size of the flyer to be A5.

Target Market(s)

FITNESS

Industry/Entity Type

Gym

Colors
33a6d7
ffffff

Requirements
Must have
• We just want to recreate the flyer but we must have the following info on the flyer and we want our timetable on the back of the flyer which you can get from this link: http://www.briskwatermotiongym.com/timetable
• Briskwater Motion Gym is a fun community of humble people. Our goal is to help guide you towards a fitter, healthier lifestyle!
• Our Programs
• HIIT
• High intensity interval training is 30-45 minutes of fat burning fun. The class is a mix of cardio, bodyweight and some resistance movements.
• Conditioning
• A full hour of strength, cardio and bodyweight training to get you in tip top shape. Expect a mix of barbells, kettlebells, rowing machines, bikes and other training methods.
• KPL
• This is our big Friday session to set you up for the weekend. 90 minutes of hard training that is done with a team emphasis. From heavy lifting to cardio triathlons, this class has it all but not for the faint hearted.
• Muay Thai
• Commonly known as the science of 8 limbs you will learn how to punch, kick, knee and elbow. Thailands national sport is a great way to get your fitness kick. We train the complete beginner all the way to international fighters so you are in great hands.
• Kids Muay Thai
• Our junior program starts from age 6 onwards. Muay Thai is a great way for kids to get active and fit while learning new skills. Training in martial arts also teaches self discipline and socialisation skills.
• Yoga
• A combination of physical and mental practises that will leave you focused and refreshed for whatever the week throws at you. We always recommend our yoga classes as a great way to balance the high intensity training we offer.
• U-Press
• Strength training with a little bit of conditioning. We regularly update the program and re test lifts to ensure you are making progress and getting stronger.
• CONTACT US
• OUR LOCATION:
• Unit 42C
• 273 Quillan Street
• Fenwick Hollow
• Glasgow
• G72TR
• Phone: 07950362814
• Email: info@briskwatermotiongym.com
• Web: www.briskwatermotiongym.com
Nice to have
• Can use all the picture but if not be good to use the boxing one and the group training one.

```html
<!DOCTYPE html>
<html lang="en">
<head>
<meta charset="utf-8">
<title>Briskwater Motion Gym – Flyer</title>
<link href="https://fonts.googleapis.com/css2?family=Archivo+Black&family=Raleway:wght@400;500;700&family=Roboto+Condensed:wght@700&display=swap" rel="stylesheet">
<style>
:root{
  --blue:#33a6d7;
  --blue-light:#3db4ea;
  --blue-mid:#2a9ed9;
  --blue-deep:#1c8ccb;
  --navy:#0e2a47;
  --white:#ffffff;
  --photo-dark:#2d2f33;
  --photo-mid:#5a5e63;
}
*{margin:0;padding:0;box-sizing:border-box}
html,body{width:851px;height:1200px;overflow:hidden;background:var(--blue)}
.flyer{position:relative;width:851px;height:1200px;overflow:hidden;font-family:"Raleway",sans-serif;color:var(--white)}
.shapes{position:absolute;left:0;top:0}
.brand{position:absolute;font-family:"Archivo Black",sans-serif;color:var(--white);line-height:1;letter-spacing:1px}
.brand--front{left:34px;top:30px;font-size:27px}
.brand--back{left:54px;top:630px;font-size:27px}
.intro{position:absolute;left:34px;top:148px;width:230px;font-size:12.5px;line-height:16px;font-weight:500}
.intro p+p{margin-top:16px}
.contact{position:absolute;top:281px;font-size:8.6px;line-height:10.5px;font-weight:700;font-family:"Raleway",sans-serif}
.contact--location{left:34px}
.contact--phone{left:132px}
.contact .gap{display:block;height:10.5px}
.programs-title{position:absolute;left:357px;top:361px;font-family:"Archivo Black",sans-serif;font-size:22px;letter-spacing:-.5px}
.program{position:absolute;width:212px}
.program h3{font-family:"Archivo Black",sans-serif;font-size:15px;line-height:16px;font-weight:400}
.program p{font-size:7.6px;line-height:10px;color:var(--navy);font-weight:500}
.timeline{position:absolute;left:0;top:0}
.timetable-title{position:absolute;right:36px;top:636px;font-family:"Archivo Black",sans-serif;font-size:30px}
.day{position:absolute;text-align:right;font-family:"Roboto Condensed",sans-serif;font-weight:700;font-size:11.5px;line-height:17.1px;text-transform:uppercase;white-space:nowrap}
.day h2{font-family:"Archivo Black",sans-serif;font-weight:400;font-size:25px;line-height:26px;color:var(--navy);margin-bottom:9px;letter-spacing:-.5px}
.day .time{color:var(--navy)}
.day .class{color:var(--white)}
</style>
</head>
<body>
<div class="flyer">
  <svg class="shapes" width="851" height="1200" viewBox="0 0 851 1200">
    <defs>
      <linearGradient id="groupTones" x1="0" y1="0" x2="1" y2="1">
        <stop offset="0" stop-color="#4a4c50"/><stop offset=".5" stop-color="#2e3034"/><stop offset="1" stop-color="#3d4a3c"/>
      </linearGradient>
      <linearGradient id="boxingTones" x1="0" y1="0" x2="1" y2="1">
        <stop offset="0" stop-color="#6b5a52"/><stop offset=".5" stop-color="#8d7a70"/><stop offset="1" stop-color="#3f4347"/>
      </linearGradient>
    </defs>
    <rect width="851" height="1200" fill="var(--blue)"/>
    <!-- front panel bands -->
    <polygon points="0,0 292,0 292,122 62,112 50,124 38,112 0,110" fill="var(--blue-light)"/>
    <polygon points="0,110 38,112 50,124 62,112 292,122 292,252 0,262" fill="var(--blue-mid)"/>
    <polygon points="0,262 292,252 292,340 0,340" fill="var(--blue-light)"/>
    <!-- back header band -->
    <polygon points="0,600 851,600 851,688 150,700 140,710 130,700 0,700" fill="var(--blue-light)"/>
    <polygon points="0,700 130,700 140,710 150,700 851,688 851,1180 0,1190" fill="var(--blue-deep)"/>
    <!-- photo areas -->
    <polygon points="292,0 851,0 851,298 292,331" fill="url(#groupTones)" role="img" aria-label="Photo: group class training with kettlebells and medicine balls in the gym"/>
    <polygon points="0,344 290,336 290,600 0,600" fill="url(#boxingTones)" role="img" aria-label="Photo: woman boxing on pads in the ring"/>
  </svg>

  <div class="brand brand--front">BRISKWATER<br>MOTION</div>

  <div class="intro">
    <p>Briskwater Motion Gym is a fun community of humble people.</p>
    <p>Our goal is to help guide you towards a fitter, healthier lifestyle!</p>
  </div>

  <div class="contact contact--location">OUR LOCATION:<br>Unit 42C<br>273 Quillan Street<br>Fenwick Hollow<br>Glasgow<br>G72TR</div>
  <div class="contact contact--phone">PHONE:<br>0795 036 28 14<span class="gap"></span>www.briskwatermotiongym.com</div>

  <h1 class="programs-title">OUR PROGRAMS</h1>

  <svg class="timeline" width="851" height="600" viewBox="0 0 851 600">
    <g stroke="var(--white)" stroke-width="2"><line x1="358" y1="412" x2="358" y2="533"/><line x1="582" y1="334" x2="582" y2="541"/></g>
    <g fill="var(--white)">
      <circle cx="358" cy="412" r="13"/><circle cx="358" cy="474" r="13"/><circle cx="358" cy="533" r="13"/>
      <circle cx="582" cy="334" r="13"/><circle cx="582" cy="414" r="13"/><circle cx="582" cy="474" r="13"/><circle cx="582" cy="541" r="13"/>
    </g>
    <g fill="var(--blue)">
      <rect x="352" y="406" width="12" height="12" rx="1"/>
      <g><circle cx="358" cy="468" r="2.3"/><rect x="356" y="471" width="4" height="8"/><rect x="351" y="472" width="14" height="2"/></g>
      <g><circle cx="358" cy="527" r="2.3"/><polygon points="352,531 364,531 361,540 355,540"/></g>
      <g><circle cx="582" cy="328" r="2.3"/><polygon points="579,331 585,331 590,338 584,336 583,341 580,341"/></g>
      <g><circle cx="578" cy="408" r="2"/><circle cx="587" cy="408" r="2"/><rect x="575" y="411" width="15" height="3"/><rect x="576" y="414" width="3" height="6"/><rect x="586" y="414" width="3" height="6"/></g>
      <g><circle cx="582" cy="468" r="2.3"/><polygon points="574,480 590,480 584,472 580,472"/></g>
      <g><circle cx="582" cy="535" r="2.3"/><rect x="580" y="538" width="4" height="8"/><rect x="575" y="538" width="14" height="2"/></g>
    </g>
  </svg>

  <div class="program" style="left:384px;top:407px"><h3>HIIT</h3><p>High intensity interval training is 30-45 minutes of fat burning fun. The class is a mix of cardio, bodyweight and some resistance movements.</p></div>
  <div class="program" style="left:384px;top:467px"><h3>CONDITIONING</h3><p>A full hour of strength, cardio and bodyweight training to get you in tip top shape. Expect a mix of barbells, kettlebells, rowing machines, bikes and other training methods.</p></div>
  <div class="program" style="left:384px;top:527px"><h3>KPL</h3><p>This is our big Friday session to set you up for the weekend. 90 minutes of hard training that is done with a team emphasis. From heavy lifting to cardio triathlons, this class has it all but not for the faint hearted.</p></div>
  <div class="program" style="left:605px;top:327px"><h3>MUAY THAI</h3><p>Commonly known as the science of 8 limbs you will learn how to punch, kick, knee and elbow. Thailands national sport is a great way to get your fitness kick. We train the complete beginner all the way to international fighters so you are in great hands.</p></div>
  <div class="program" style="left:605px;top:407px"><h3>KIDS MUAY THAI</h3><p>Our junior program starts from age 6 onwards. Muay Thai is a great way for kids to get active and fit while learning new skills. Training in martial arts also teaches self discipline and socialisation skills.</p></div>
  <div class="program" style="left:605px;top:467px"><h3>YOGA</h3><p>A combination of physical and mental practices that will leave you focused and refreshed for whatever the week throws at you. We always recommend our yoga classes as a great way to balance the high intensity training we offer.</p></div>
  <div class="program" style="left:605px;top:534px"><h3>U-PRESS</h3><p>Strength training with a little bit of conditioning. We regularly update the program and re test lifts to ensure you are making progress and getting stronger.</p></div>

  <div class="brand brand--back">BRISKWATER<br>MOTION</div>
  <div class="timetable-title">TIMETABLE</div>

  <div class="day" style="right:593px;top:737px"><h2>MON</h2>
    <div><span class="time">7AM</span> <span class="class">Conditioning</span></div>
    <div><span class="time">8AM</span> <span class="class">Open Gym</span></div>
    <div><span class="time">10AM</span> <span class="class">U-Press</span></div>
    <div><span class="time">12:10PM</span> <span class="class">Lunch Time HIIT</span></div>
    <div><span class="time">4PM</span> <span class="class">Open Gym</span></div>
    <div><span class="time">5PM</span> <span class="class">U-Press</span></div>
    <div><span class="time">6PM</span> <span class="class">Fundamentals</span></div>
    <div><span class="time">6PM</span> <span class="class">Muay Thai Foundations</span></div>
    <div><span class="time">7PM</span> <span class="class">Strength and Conditioning</span></div>
  </div>
  <div class="day" style="right:409px;top:737px"><h2>TUE</h2>
    <div><span class="time">6AM</span> <span class="class">U-Press</span></div>
    <div><span class="time">7AM</span> <span class="class">Fight Camp Muay Thai</span></div>
    <div><span class="time">8AM</span> <span class="class">Open Gym</span></div>
    <div><span class="time">12:10PM</span> <span class="class">Lunch Time HIIT</span></div>
    <div><span class="time">4PM</span> <span class="class">Open Gym</span></div>
    <div><span class="time">5:15PM</span> <span class="class">HIIT (0/30)</span></div>
    <div><span class="time">6PM</span> <span class="class">Conditioning</span></div>
    <div><span class="time">6PM</span> <span class="class">Kids</span></div>
    <div><span class="time">7PM</span> <span class="class">Muay Thai Intermediate</span></div>
  </div>
  <div class="day" style="right:591px;top:952px"><h2>WED</h2>
    <div><span class="time">6AM</span> <span class="class">Strength and Conditioning</span></div>
    <div><span class="time">7AM</span> <span class="class">Yoga (0/25)</span></div>
    <div><span class="time">8AM</span> <span class="class">Open Gym</span></div>
    <div><span class="time">10AM</span> <span class="class">U-Press</span></div>
    <div><span class="time">4PM</span> <span class="class">Open Gym</span></div>
    <div><span class="time">5PM</span> <span class="class">U-Press</span></div>
    <div><span class="time">5:15PM</span> <span class="class">HIIT (0/30)</span></div>
    <div><span class="time">6PM</span> <span class="class">Fundamentals</span></div>
    <div><span class="time">6PM</span> <span class="class">Muay Thai Foundations</span></div>
    <div><span class="time">7:15PM</span> <span class="class">Yoga (0/25)</span></div>
  </div>
  <div class="day" style="right:407px;top:952px"><h2>THU</h2>
    <div><span class="time">7AM</span> <span class="class">Conditioning</span></div>
    <div><span class="time">8AM</span> <span class="class">Open Gym</span></div>
    <div><span class="time">12:10PM</span> <span class="class">Lunch Time HIIT</span></div>
    <div><span class="time">4PM</span> <span class="class">Open Gym</span></div>
    <div><span class="time">5:15PM</span> <span class="class">HIIT (0/30)</span></div>
    <div><span class="time">6PM</span> <span class="class">Conditioning</span></div>
    <div><span class="time">6PM</span> <span class="class">Kids</span></div>
    <div><span class="time">7PM</span> <span class="class">Muay Thai Intermediate</span></div>
  </div>
  <div class="day" style="right:231px;top:952px"><h2>FRI</h2>
    <div><span class="time">6AM</span> <span class="class">U-Press</span></div>
    <div><span class="time">7AM</span> <span class="class">Fight Camp Muay Thay</span></div>
    <div><span class="time">8AM</span> <span class="class">Open Gym</span></div>
    <div><span class="time">10AM</span> <span class="class">U-Press</span></div>
    <div><span class="time">12:10PM</span> <span class="class">Lunch Time HIIT</span></div>
    <div><span class="time">4PM</span> <span class="class">Open Gym</span></div>
    <div><span class="time">5PM</span> <span class="class">U-Press</span></div>
    <div><span class="time">6PM</span> <span class="class">KPL</span></div>
  </div>
  <div class="day" style="right:43px;top:952px"><h2>SAT</h2>
    <div><span class="time">10AM</span> <span class="class">Saturday Circuit</span></div>
    <div><span class="time">11AM</span> <span class="class">Open Gym</span></div>
    <div><span class="time">11AM</span> <span class="class">Fundamentals</span></div>
    <div><span class="time">11AM</span> <span class="class">Kids</span></div>
    <div><span class="time">12PM</span> <span class="class">Muay Thai Foundations</span></div>
  </div>
</div>
</body>
</html>
```